Dog themed post card for homeowners that may be willing to sell their house.

We will be sending these postcards to homeowners that may be interested in selling their house. Our business is themed around our dog "Wexley"- Wexley Buys Houses. We are using her as the focal point of the business because typically these homeowners get lots of mailers that are similar and we would like stand out with an inviting puppy dog.
We would like to included the icon for facebook and instragam with her handle "@WexleyBuysHouses" and her website WexleyBuysHouses.example and our phone number 555-814-2760.
We will be sending these postcards in batches to various subdivisions. For that reason please consider a format that can easily change the name of the subdivision. We are including the subdivision name because we want the postcard to be slightly more personal/targeted.
Our business is just starting and we would like to get some brand recognition going. We envision Wexley Buys Houses predominately displayed somehow.
I have attached numerous pictures of Wexley. We envision using one on each side of the postcard. Below are phrases we would like to include on the postcard in a format that you see fitting. Please use the verbiage below and not what is sketched on the uploaded postcard. The below verbiage is the most up to date.
-I recently bought a house in (subdivision name) and would love to buy yours.
-Call my humans today so we can give you a no obligation offer
-No money out of your pocket
-Quick closing
-Any condition
-Can help with moving expenses

Target Market(s)

Home owners with equity in their house that may need to sell quickly. These are generally people that do not enjoy the buying/selling of real estate. It can sometimes be someone who has recently inherited a home and doesnt want to deal with the headache. Other times it may be someone going through a divorce or forclosure and want to sell their home quickly.

Industry/Entity Type

Direct Marketing

Requirements
Must have
• Happy and bright feel. This industry is saturated with less than ethical people and we are trying to convey a very clean, honest, straight forward and scam-free process.

```html
<!DOCTYPE html>
<html lang="en">
<head>
<meta charset="utf-8">
<title>Wexley Buys Houses – Postcard</title>
<link href="https://fonts.googleapis.com/css2?family=Montserrat:wght@500;600;700;800&family=Oswald:wght@400;500;600;700&display=swap" rel="stylesheet">
<style>
  :root{
    --purple:#35277a;
    --yellow:#f4c521;
    --gold:#d8b12c;
    --charcoal:#2e2e2e;
    --slate:#4f4f4f;
    --paper:#ffffff;
    --page:#e6e6e6;
    --ink:#262626;
    --rule:#b9b9b9;
  }
  *{box-sizing:border-box;margin:0;padding:0}
  html,body{width:900px;height:1200px;overflow:hidden;background:var(--page)}
  body{position:relative;font-family:"Montserrat",sans-serif;color:var(--ink)}
  .postcard{position:absolute;left:70px;width:760px;height:548px;background:var(--paper);box-shadow:0 6px 18px rgba(0,0,0,.18);overflow:hidden}
  .postcard--front{top:40px}
  .postcard--back{top:612px}
  .postcard__art{position:absolute;inset:0;width:100%;height:100%}
  .abs{position:absolute}

  /* front */
  .logo-word{font-family:"Montserrat",sans-serif;font-weight:800;letter-spacing:1px;color:var(--ink)}
  .front__logo{left:36px;top:34px;font-size:38px}
  .front__name{left:36px;top:90px;font-family:"Oswald",sans-serif;font-weight:400;font-size:44px;line-height:1;color:var(--ink);letter-spacing:-.5px}
  .front__buys{left:32px;top:130px;font-family:"Oswald",sans-serif;font-weight:700;font-size:118px;line-height:1;color:var(--purple);letter-spacing:-3px}
  .front__houses{left:34px;top:238px;font-family:"Oswald",sans-serif;font-weight:700;font-size:80px;line-height:1;color:var(--purple);letter-spacing:-2px}
  .price__label{left:36px;top:342px;font-family:"Oswald",sans-serif;font-weight:600;font-size:29px;line-height:.85;color:var(--charcoal)}
  .price__value{left:148px;top:340px;font-family:"Oswald",sans-serif;font-weight:500;font-size:58px;line-height:1;color:var(--paper)}
  .price__value sup{font-size:26px;vertical-align:top;position:relative;top:4px}
  .front__web{left:36px;top:426px;display:flex;align-items:center;gap:10px;font-weight:700;font-size:18px;color:var(--ink)}
  .front__phone{left:36px;top:466px;display:flex;align-items:center;gap:10px;font-weight:700;font-size:40px;color:var(--paper);letter-spacing:.5px}
  .front__social{left:36px;top:514px}

  .social{display:flex;gap:22px;font-size:12px;font-weight:500;color:#dcdcdc}
  .social span{display:flex;align-items:center;gap:6px}
  .social i{display:inline-block;width:12px;height:12px;border-radius:50%;background:#e8e8e8}

  /* back */
  .back__lead{left:15px;top:259px;width:380px;font-weight:700;font-size:14px;line-height:1.25;color:var(--purple)}
  .back__call{left:15px;top:318px;width:380px;font-weight:700;font-size:17.5px;line-height:1.25;color:var(--paper);text-transform:uppercase;letter-spacing:.6px}
  .benefits{left:15px;top:384px;display:grid;grid-template-columns:172px 190px;row-gap:10px;column-gap:4px;font-size:11.5px;font-weight:600;line-height:1.1;color:var(--slate)}
  .benefit{display:flex;align-items:center;gap:10px}
  .benefit svg{flex:none}
  .back__phone{left:15px;top:476px;display:flex;align-items:center;gap:8px;font-weight:700;font-size:28px;color:var(--paper)}
  .back__social{left:15px;top:518px;font-size:10.5px;gap:16px}
  .back__social i{width:11px;height:11px}
  .back__logo{left:470px;top:38px;font-size:27px}
  .stamp-box{left:652px;top:17px;width:79px;height:77px;border:1.5px solid var(--rule)}
  .address-line{left:477px;width:253px;height:0;border-top:1.5px solid var(--rule)}
</style>
</head>
<body>

<!-- FRONT -->
<section class="postcard postcard--front" aria-label="Postcard front">
  <svg class="postcard__art" viewBox="0 0 590 425" preserveAspectRatio="none" aria-hidden="false">
    <rect width="590" height="425" fill="var(--paper)"/>
    <rect x="0" y="261" width="106" height="58" fill="var(--gold)"/>
    <rect x="106" y="261" width="240" height="58" fill="var(--purple)"/>
    <rect x="0" y="355" width="590" height="70" fill="var(--charcoal)"/>
    <path d="M250 0 C208 130 214 305 458 425 L590 425 L590 0 Z" fill="var(--yellow)"/>
    <g role="img" aria-label="Photo of Wexley, a fluffy grey and white dog wearing a bandana, sitting in front of a white brick house">
      <defs>
        <linearGradient id="frontPhoto" x1="0" y1="0" x2="0" y2="1">
          <stop offset="0" stop-color="#8d8f94"/>
          <stop offset=".45" stop-color="#d9dadd"/>
          <stop offset=".75" stop-color="#a9a6a3"/>
          <stop offset="1" stop-color="#7d6a57"/>
        </linearGradient>
      </defs>
      <path d="M262 0 C222 130 228 300 474 418 L590 418 L590 0 Z" fill="url(#frontPhoto)"/>
    </g>
  </svg>

  <div class="abs logo-word front__logo">LOGO</div>
  <div class="abs front__name">WEXLEY</div>
  <div class="abs front__buys">BUYS</div>
  <div class="abs front__houses">HOUSES</div>
  <div class="abs price__label">PRICE<br>FOR</div>
  <div class="abs price__value"><sup>$</sup>000,000</div>
  <div class="abs front__web">
    <svg width="18" height="18" viewBox="0 0 20 20" aria-hidden="true"><circle cx="10" cy="10" r="9" fill="none" stroke="var(--purple)" stroke-width="2"/><ellipse cx="10" cy="10" rx="4" ry="9" fill="none" stroke="var(--purple)" stroke-width="1.6"/><path d="M1 10H19M3 5.5H17M3 14.5H17" stroke="var(--purple)" stroke-width="1.4"/></svg>
    WexleyBuysHouses.example
  </div>
  <div class="abs front__phone">
    <svg width="38" height="38" viewBox="0 0 40 40" aria-hidden="true"><circle cx="20" cy="20" r="17" fill="none" stroke="#fff" stroke-width="3.2"/><path d="M14 11c1.5-1 3 0 3.6 1.6l1 2.6c.4 1-.1 2-1 2.6l-1 .6c.8 2.4 2.6 4.3 5 5.2l.6-1c.6-.9 1.6-1.3 2.6-.9l2.6 1c1.6.6 2.6 2.1 1.6 3.6-1.3 2-3.4 2.7-5.6 2-5.4-1.8-9.4-5.8-11.2-11.2-.7-2.2 0-4.3 2-5.6z" fill="#fff"/></svg>
    555-814-2760
  </div>
  <div class="abs social front__social">
    <span><i></i>@WexleyBuysHouses</span>
    <span><i></i>@WexleyBuysHouses</span>
  </div>
</section>

<!-- BACK -->
<section class="postcard postcard--back" aria-label="Postcard back">
  <svg class="postcard__art" viewBox="0 0 590 425" preserveAspectRatio="none">
    <defs>
      <clipPath id="backPanel"><path d="M0 0 L220 0 C296 62 312 300 262 425 L0 425 Z"/></clipPath>
      <linearGradient id="backPhoto" x1="0" y1="0" x2="1" y2="1">
        <stop offset="0" stop-color="#d8d9db"/>
        <stop offset=".55" stop-color="#b8b7b4"/>
        <stop offset="1" stop-color="#6f5f4c"/>
      </linearGradient>
    </defs>
    <rect width="590" height="425" fill="var(--paper)"/>
    <path d="M0 0 L240 0 C322 66 340 300 290 425 L0 425 Z" fill="var(--yellow)"/>
    <path d="M0 0 L233 0 C312 64 329 300 278 425 L0 425 Z" fill="var(--purple)"/>
    <g clip-path="url(#backPanel)">
      <rect width="340" height="425" fill="var(--paper)"/>
      <g role="img" aria-label="Photo of Wexley, a fluffy grey dog in a bandana, sitting on a sidewalk beside a garden bed">
        <rect width="340" height="186" fill="url(#backPhoto)"/>
      </g>
      <rect y="186" width="340" height="3" fill="var(--yellow)"/>
      <rect y="240" width="340" height="51" fill="var(--slate)"/>
      <rect y="362" width="340" height="63" fill="var(--charcoal)"/>
    </g>
  </svg>

  <p class="abs back__lead">I recently bought a house in (subdivision name) and would love to buy yours.</p>
  <p class="abs back__call">Call my humans today so we can give you a no obligation offer</p>

  <ul class="abs benefits" style="list-style:none">
    <li class="benefit"><svg width="20" height="20" viewBox="0 0 20 20" aria-hidden="true"><circle cx="10" cy="10" r="10" fill="var(--yellow)"/><path d="M5.5 10.5l3 3 6-6.5" fill="none" stroke="var(--purple)" stroke-width="2"/></svg>No money out of<br>your pocket</li>
    <li class="benefit"><svg width="20" height="20" viewBox="0 0 20 20" aria-hidden="true"><circle cx="10" cy="10" r="10" fill="var(--yellow)"/><path d="M5.5 10.5l3 3 6-6.5" fill="none" stroke="var(--purple)" stroke-width="2"/></svg>Any condition</li>
    <li class="benefit"><svg width="20" height="20" viewBox="0 0 20 20" aria-hidden="true"><circle cx="10" cy="10" r="10" fill="var(--yellow)"/><path d="M5.5 10.5l3 3 6-6.5" fill="none" stroke="var(--purple)" stroke-width="2"/></svg>Quick closing</li>
    <li class="benefit"><svg width="20" height="20" viewBox="0 0 20 20" aria-hidden="true"><circle cx="10" cy="10" r="10" fill="var(--yellow)"/><path d="M5.5 10.5l3 3 6-6.5" fill="none" stroke="var(--purple)" stroke-width="2"/></svg>Can help with moving<br>expenses</li>
  </ul>

  <div class="abs back__phone">
    <svg width="28" height="28" viewBox="0 0 40 40" aria-hidden="true"><circle cx="20" cy="20" r="17" fill="none" stroke="#fff" stroke-width="3.5"/><path d="M14 11c1.5-1 3 0 3.6 1.6l1 2.6c.4 1-.1 2-1 2.6l-1 .6c.8 2.4 2.6 4.3 5 5.2l.6-1c.6-.9 1.6-1.3 2.6-.9l2.6 1c1.6.6 2.6 2.1 1.6 3.6-1.3 2-3.4 2.7-5.6 2-5.4-1.8-9.4-5.8-11.2-11.2-.7-2.2 0-4.3 2-5.6z" fill="#fff"/></svg>
    555-814-2760
  </div>
  <div class="abs social back__social">
    <span><i></i>@WexleyBuysHouses</span>
    <span><i></i>@WexleyBuysHouses</span>
  </div>

  <div class="abs logo-word back__logo">LOGO</div>
  <div class="abs stamp-box" aria-label="Stamp area"></div>
  <div class="abs address-line" style="top:191px"></div>
  <div class="abs address-line" style="top:247px"></div>
  <div class="abs address-line" style="top:304px"></div>
  <div class="abs address-line" style="top:361px"></div>
</section>

</body>
</html>
```